Design Packaging for Monte Alba Coffee

Please look at website at www.montealbacoffeecompany.example
Need packaging for new coffee company. The size is: 6 x 9 x 3"

```html
<!DOCTYPE html>
<html lang="en">
<head>
<meta charset="UTF-8">
<title>Monte Alba Coffee – Cocoa Beans Label</title>
<link href="https://fonts.googleapis.com/css2?family=Montserrat:wght@600;700;800;900&family=Saira+Condensed:wght@600&display=swap" rel="stylesheet">
<style>
  :root {
    --backdrop: #e8ecee;
    --label-white: #ffffff;
    --cocoa-dark: #2f1c19;
    --text-light: #ffffff;
    --brand-tone: #7d5f33;
    --pod-light: #ece6df;
    --pod-mid: #b9aca0;
  }
  html, body {
    margin: 0;
    width: 1200px;
    height: 866px;
    overflow: hidden;
    background: var(--backdrop);
  }
  .label {
    position: absolute;
    left: 340px;
    top: 43px;
    width: 520px;
    height: 780px;
    background: var(--label-white);
    box-shadow: 6px 8px 14px rgba(0,0,0,0.18);
  }
  .brand {
    position: absolute;
    top: 176px;
    left: 0;
    width: 100%;
    display: flex;
    justify-content: center;
    align-items: center;
    gap: 10px;
  }
  .brand-dot {
    width: 14px;
    height: 14px;
    border-radius: 50%;
    background: var(--brand-tone);
  }
  .brand-name {
    font-family: "Saira Condensed", "Arial Narrow", sans-serif;
    font-weight: 600;
    font-size: 30px;
    letter-spacing: 0.5px;
    color: var(--brand-tone);
    text-transform: uppercase;
  }
  .pod-illustration {
    position: absolute;
    left: 155px;
    top: 228px;
    width: 195px;
    height: 154px;
  }
  .info-panel {
    position: absolute;
    left: 85px;
    top: 381px;
    width: 350px;
    height: 399px;
    background: var(--cocoa-dark);
    color: var(--text-light);
    font-family: "Montserrat", Arial, sans-serif;
  }
  .info-stack {
    position: absolute;
    left: 39px;
    top: 16px;
    width: 280px;
    text-align: center;
  }
  .tagline {
    font-weight: 700;
    font-size: 14.5px;
    line-height: 20px;
    padding-bottom: 4px;
    border-bottom: 1.5px solid var(--text-light);
    white-space: nowrap;
  }
  .quality {
    font-weight: 800;
    font-size: 24px;
    line-height: 30px;
    padding: 5px 0 3px;
    border-bottom: 1.5px solid var(--text-light);
  }
  .product-name {
    font-weight: 900;
    font-size: 81px;
    line-height: 70px;
    padding: 10px 0 9px;
    letter-spacing: -1px;
    border-bottom: 1.5px solid var(--text-light);
  }
  .qualities {
    font-weight: 700;
    font-size: 30px;
    line-height: 38px;
    padding: 2px 0 2px;
    border-bottom: 1.5px solid var(--text-light);
  }
  .vegan {
    font-weight: 800;
    font-size: 30px;
    line-height: 40px;
    letter-spacing: 4px;
    padding-top: 2px;
    white-space: nowrap;
  }
</style>
</head>
<body>
  <main class="label">
    <div class="brand">
      <span class="brand-dot"></span>
      <span class="brand-name">Monte Alba Coffee</span>
    </div>

    <svg class="pod-illustration" role="img" aria-label="Line drawing of three cacao pods, the middle one cut open to show its beans" viewBox="0 0 195 154">
      <defs>
        <linearGradient id="podTone" x1="0" y1="0" x2="0" y2="1">
          <stop offset="0" stop-color="var(--pod-light)"/>
          <stop offset="1" stop-color="var(--pod-mid)"/>
        </linearGradient>
      </defs>
      <rect width="195" height="154" fill="url(#podTone)"/>
    </svg>

    <section class="info-panel">
      <div class="info-stack">
        <div class="tagline">100% ORGANIC FOOD HEALTHY</div>
        <div class="quality">PREMIUM QUALITY</div>
        <h1 class="product-name" style="margin:0">COCA<br>BEANS</h1>
        <div class="qualities">Organic | Fresh</div>
        <div class="vegan">100% VEGAN</div>
      </div>
    </section>
  </main>
</body>
</html>
```